Boutique custom software development company needs new business card

Our nearly 20 year old custom software development company would like to better include the fact that we are now providing Bitcoin services. These new services are B2B include education (how to acquire and securely hold Bitcoin) and integrating Bitcoin payments into existing ecommerce sites or other existing systems. Please keep the card clean and simple. Attached is our current design and some other files. vexalon.example

Target Market(s)

businesses owners interested in long term relationship

Industry/Entity Type

Custom software development and Bitcoin

Contact Information for Business Card

Marcus Ellwood, marcus@vexalon.example, vexalon.example, (888) 555-VEXAL

Font styles to use
Other font styles liked:
• monospace

Requirements
Must have
• double-sided
Nice to have
• clean and simple
Should not have
• physical address

```html
<!DOCTYPE html>
<html lang="en">
<head>
<meta charset="utf-8">
<title>Vexalon Business Card</title>
<link rel="stylesheet" href="https://fonts.googleapis.com/css2?family=Source+Code+Pro:wght@400;600;700&family=Lato:wght@400&display=swap">
<style>
  :root {
    --backdrop: #5f5e5f;
    --brand-blue: #3e71b7;
    --brand-orange: #f07b22;
    --paper: #ffffff;
    --mono: "Source Code Pro", monospace;
    --sans: "Lato", sans-serif;
  }
  * { margin: 0; padding: 0; box-sizing: border-box; }
  html, body { width: 1200px; height: 1200px; overflow: hidden; }
  body { background: var(--backdrop); position: relative; }

  .card {
    position: absolute;
    left: 250px;
    width: 700px;
    height: 400px;
    overflow: hidden;
    box-shadow: 2px 3px 6px rgba(0,0,0,0.35);
  }
  .card--front { top: 170px; background: var(--paper); }
  .card--back { top: 631px; background: var(--brand-blue); }

  .front-swoosh { position: absolute; inset: 0; width: 700px; height: 400px; }

  .brand-mark {
    position: absolute;
    right: 84px;
    top: 100px;
    display: flex;
    align-items: center;
    gap: 10px;
  }
  .brand-mark__square {
    width: 26px; height: 26px;
    background: var(--brand-orange);
  }
  .brand-mark__name {
    font-family: var(--mono);
    font-weight: 700;
    font-size: 34px;
    color: var(--brand-blue);
    letter-spacing: 1px;
  }

  .contact { position: absolute; left: 47px; top: 238px; color: var(--paper); }
  .contact__name {
    font-family: var(--mono);
    font-weight: 600;
    font-size: 30px;
    letter-spacing: 1px;
    line-height: 1;
    margin-bottom: 14px;
  }
  .contact__list { list-style: none; }
  .contact__item {
    display: flex;
    align-items: center;
    gap: 11px;
    font-family: var(--mono);
    font-size: 17px;
    height: 24.5px;
  }
  .contact__icon { width: 14px; height: 14px; flex: none; }

  .back-brand {
    position: absolute;
    left: 0; right: 0;
    top: 128px;
    text-align: center;
    color: var(--paper);
  }
  .back-brand__name {
    font-family: var(--mono);
    font-weight: 700;
    font-size: 96px;
    line-height: 1;
    letter-spacing: 2px;
  }
  .back-brand__tagline {
    font-family: var(--sans);
    font-size: 30px;
    letter-spacing: -1.2px;
    margin-top: 12px;
  }
</style>
</head>
<body>

<section class="card card--front">
  <svg class="front-swoosh" viewBox="0 0 700 400" aria-hidden="true">
    <path d="M0,107 Q345,158 493,400 L463,400 Q320,172 0,107 Z" fill="var(--brand-orange)"/>
    <path d="M0,107 Q320,172 463,400 L0,400 Z" fill="var(--brand-blue)"/>
    <path d="M0,107 Q320,172 463,400" fill="none" stroke="var(--paper)" stroke-width="1.2"/>
  </svg>

  <div class="brand-mark">
    <span class="brand-mark__square"></span>
    <span class="brand-mark__name">VEXALON</span>
  </div>

  <div class="contact">
    <h1 class="contact__name">MARCUS ELLWOOD</h1>
    <ul class="contact__list">
      <li class="contact__item">
        <svg class="contact__icon" viewBox="0 0 16 16" aria-hidden="true">
          <path d="M3.5 1.5 L6 4.5 L4.8 6 Q6.5 9.5 10 11.2 L11.5 10 L14.5 12.5 L12.8 14.5 Q6 14 1.5 3.2 Z" fill="var(--paper)"/>
          <path d="M9 2 A5 5 0 0 1 14 7 M9 4.5 A2.5 2.5 0 0 1 11.5 7" fill="none" stroke="var(--paper)" stroke-width="1.3"/>
        </svg>
        <span>(888) 555-VEXAL</span>
      </li>
      <li class="contact__item">
        <svg class="contact__icon" viewBox="0 0 16 16" aria-hidden="true">
          <rect x="1" y="3.5" width="14" height="9.5" fill="none" stroke="var(--paper)" stroke-width="1.3"/>
          <path d="M1 3.5 L8 9 L15 3.5 M1 13 L6 8 M15 13 L10 8" fill="none" stroke="var(--paper)" stroke-width="1.1"/>
        </svg>
        <span>marcus@vexalon.example</span>
      </li>
      <li class="contact__item">
        <svg class="contact__icon" viewBox="0 0 16 16" aria-hidden="true">
          <circle cx="8" cy="8" r="6.8" fill="none" stroke="var(--paper)" stroke-width="1.4"/>
          <path d="M4 4.5 Q6.5 4 6.8 6.5 Q5 8 6 10.5 L4.5 12 Q3 9 4 4.5 Z M9 3 Q12 4 12.5 7 Q10.5 8.5 9.5 6.5 Z M9 10 L12 10 L10 13 Z" fill="var(--paper)"/>
        </svg>
        <span>vexalon.example</span>
      </li>
    </ul>
  </div>
</section>

<section class="card card--back">
  <div class="back-brand">
    <div class="back-brand__name">VEXALON</div>
    <p class="back-brand__tagline">developer of custom applications</p>
  </div>
</section>

</body>
</html>
```